Lumen Path - Fiber Internet to the home postcard

Design a postcard for my company, Lumen Path, using the logo below. On the front of the card:
- No Buffering • No BS
- Second line should be the logo
- $60 / month • 10-Gigs
- lumenpath.net

Color palate should follow the colors in the logo.

Address should say
- Special pricing during construction
- Our best price
- Our fastest speed
- $60 / month • 10-Gigs
- lumenpath.net

Target Market(s)

25 - 55 year olds. Middle income/class. People with kids and pick up trucks

Industry/Entity Type

Fiber Internet Service Provider

Font styles to use
Sans Serif

Colors

Designer to choose colors to be used in the design.

Requirements
Nice to have
• I am open to more creative changes

```html
<!DOCTYPE html>
<html lang="en">
<head>
<meta charset="utf-8">
<title>Lumen Path – Fiber Internet Postcard</title>
<link rel="stylesheet" href="https://fonts.googleapis.com/css2?family=Montserrat:wght@400;600;700;800;900&display=swap">
<style>
  :root {
    --navy: #0b2a62;
    --navy-deep: #081f4d;
    --green: #7ac143;
    --green-light: #b5dc95;
    --blue: #1f63d8;
    --white: #ffffff;
    --stage: #bfbfbf;
    --ink-line: #3a3a3a;
  }
  * { margin: 0; padding: 0; box-sizing: border-box; }
  html, body { width: 916px; height: 1200px; overflow: hidden; }
  body {
    background: var(--stage);
    font-family: "Montserrat", Arial, sans-serif;
    position: relative;
  }
  .postcard {
    position: absolute;
    left: 104px;
    width: 705px;
    height: 470px;
    overflow: hidden;
    background: var(--white);
  }
  .postcard--front { top: 93px; }
  .postcard--back { top: 637px; }
  .postcard svg { display: block; width: 705px; height: 470px; }
  .t-heavy { font-weight: 900; }
  .t-bold { font-weight: 800; }
  .t-semi { font-weight: 700; }
  .t-regular { font-weight: 400; }
</style>
</head>
<body>

<!-- FRONT -->
<section class="postcard postcard--front" aria-label="Postcard front">
  <svg viewBox="0 0 705 470" xmlns="http://www.w3.org/2000/svg">
    <defs>
      <linearGradient id="fiberGlow" x1="0" y1="0" x2="1" y2="1">
        <stop offset="0" stop-color="#0b2a62" stop-opacity="0"/>
        <stop offset="0.45" stop-color="#1a4fb8"/>
        <stop offset="1" stop-color="#2a74f0"/>
      </linearGradient>
      <radialGradient id="familyPhoto" cx="0.5" cy="0.45" r="0.6">
        <stop offset="0" stop-color="#d9d4d0"/>
        <stop offset="0.55" stop-color="#a9b7cf"/>
        <stop offset="1" stop-color="#6c7f9c"/>
      </radialGradient>
      <clipPath id="frontClip"><rect width="705" height="470"/></clipPath>
    </defs>

    <g clip-path="url(#frontClip)">
      <rect class="bg-navy" width="705" height="470" fill="var(--navy)"/>
      <rect class="fiber-texture" x="260" y="0" width="445" height="330" fill="url(#fiberGlow)"
            role="img" aria-label="Blue fiber optic light strands"/>

      <path class="wave-green" d="M0,300 C120,235 300,250 420,320 C520,370 640,300 705,245 L705,470 L0,470 Z" fill="var(--green)"/>
      <path d="M0,285 C120,215 300,230 420,305" fill="none" stroke="var(--green)" stroke-width="1.2"/>
      <path d="M0,318 C140,240 320,260 440,330" fill="none" stroke="var(--navy)" stroke-width="1.2"/>
      <path d="M705,258 C640,320 560,370 480,350" fill="none" stroke="var(--navy)" stroke-width="1.2"/>

      <g class="orbits" fill="none" stroke="var(--white)" stroke-width="1">
        <path d="M329,122 A170,170 0 1 1 420,378"/>
        <path d="M352,95 A185,185 0 1 1 420,398"/>
        <path d="M380,70 A200,200 0 1 1 450,418"/>
      </g>
      <g class="orbit-dots" fill="var(--green)">
        <circle cx="329" cy="122" r="4"/>
        <circle cx="353" cy="110" r="4"/>
        <circle cx="389" cy="93" r="4"/>
      </g>
      <g fill="var(--navy)">
        <circle cx="380" cy="341" r="4"/>
        <circle cx="419" cy="381" r="4"/>
        <circle cx="450" cy="406" r="4"/>
      </g>

      <circle cx="493" cy="220" r="153" fill="#7d8fb0" opacity="0.8"/>
      <circle cx="493" cy="220" r="142" fill="url(#familyPhoto)"
              role="img" aria-label="Photo of a smiling family sharing a laptop on the sofa"/>

      <circle class="brand-dot" cx="62" cy="66" r="16" fill="var(--green)"/>
      <text class="brand-name t-bold" x="88" y="81" font-size="40" fill="var(--white)">Lumen Path</text>

      <polygon points="46,130 302,130 293,173 37,173" fill="var(--green)"/>
      <text class="t-semi" x="169" y="163" font-size="32" fill="var(--white)" text-anchor="middle">No Buffering</text>
      <polygon points="80,174 258,174 248,215 70,215" fill="var(--white)"/>
      <text class="t-semi" x="164" y="206" font-size="29" fill="var(--navy)" text-anchor="middle">No BS</text>

      <g class="price-badge">
        <circle cx="125" cy="372" r="94" fill="none" stroke="var(--white)" stroke-width="1" stroke-dasharray="2 2"/>
        <circle cx="250" cy="389" r="70" fill="none" stroke="var(--white)" stroke-width="1" stroke-dasharray="2 2"/>
        <circle cx="125" cy="372" r="88" fill="var(--green-light)"/>
        <circle cx="250" cy="389" r="64" fill="var(--green-light)"/>
        <circle cx="125" cy="372" r="80" fill="var(--white)"/>
        <circle cx="250" cy="389" r="56" fill="var(--white)"/>
        <g class="speed-icon" transform="translate(134,332)" fill="none" stroke-width="7">
          <path d="M-24,0 A24,24 0 0 1 13,-20" stroke="var(--navy)"/>
          <path d="M14,-19 A24,24 0 0 1 24,0" stroke="var(--green)"/>
          <line x1="-8" y1="10" x2="16" y2="-4" stroke="var(--navy)" stroke-width="3" stroke-linecap="round"/>
          <circle cx="-8" cy="10" r="4" fill="var(--navy)" stroke="none"/>
        </g>
        <text class="t-heavy" x="72" y="406" font-size="46" fill="var(--navy)">$60</text>
        <text class="t-heavy" x="186" y="406" font-size="50" fill="var(--navy)">/</text>
        <text class="t-heavy" x="220" y="406" font-size="48" fill="var(--green)">10</text>
        <text class="t-semi" x="91" y="428" font-size="20" fill="var(--green)">Month</text>
        <text class="t-semi" x="228" y="422" font-size="18" fill="var(--navy)">Gigs</text>
      </g>

      <text class="web t-regular" x="381" y="446" font-size="19" letter-spacing="3" fill="var(--white)">www.<tspan class="t-bold">lumenpath</tspan>.net</text>
    </g>
  </svg>
</section>

<!-- BACK -->
<section class="postcard postcard--back" aria-label="Postcard back">
  <svg viewBox="0 0 705 470" xmlns="http://www.w3.org/2000/svg">
    <defs>
      <linearGradient id="fiberBack" x1="0" y1="1" x2="1" y2="0">
        <stop offset="0" stop-color="#0b2a62"/>
        <stop offset="0.6" stop-color="#163f95"/>
        <stop offset="1" stop-color="#2a6be0"/>
      </linearGradient>
      <clipPath id="panelClip">
        <path d="M0,0 L315,0 C355,40 372,120 366,185 C358,270 290,330 290,400 C290,430 300,455 315,470 L0,470 Z"/>
      </clipPath>
    </defs>

    <rect width="705" height="470" fill="var(--white)"/>

    <path class="panel-edge" d="M0,0 L315,0 C360,40 384,120 378,185 C370,270 305,330 305,400 C305,430 315,455 345,470 L0,470 Z" fill="var(--green)"/>
    <g clip-path="url(#panelClip)">
      <rect width="705" height="470" fill="var(--navy)"/>
      <rect width="705" height="171" fill="url(#fiberBack)" role="img" aria-label="Blue fiber optic light strands"/>
      <rect y="171" width="705" height="167" fill="var(--white)"/>
    </g>

    <text class="t-heavy" x="175" y="58" font-size="24" fill="var(--green)" text-anchor="middle">Special Pricing</text>
    <text class="t-heavy" x="175" y="92" font-size="24" fill="var(--white)" text-anchor="middle">During Construction</text>

    <rect x="26" y="115" width="300" height="28" rx="14" fill="var(--white)"/>
    <rect x="162" y="115" width="170" height="28" rx="14" fill="var(--green)"/>
    <text class="t-semi" x="93" y="134" font-size="14" fill="var(--navy)" text-anchor="middle">Our best price</text>
    <text class="t-semi" x="248" y="134" font-size="14" fill="var(--white)" text-anchor="middle">Our fastest speed</text>

    <g class="speed-icon" transform="translate(160,213)" fill="none" stroke-width="7">
      <path d="M-24,0 A24,24 0 0 1 13,-20" stroke="var(--navy)"/>
      <path d="M14,-19 A24,24 0 0 1 24,0" stroke="var(--green)"/>
      <line x1="-8" y1="10" x2="16" y2="-4" stroke="var(--navy)" stroke-width="3" stroke-linecap="round"/>
      <circle cx="-8" cy="10" r="4" fill="var(--navy)" stroke="none"/>
    </g>
    <text class="t-heavy" x="160" y="265" font-size="34" text-anchor="middle" fill="var(--navy)">$60 / <tspan fill="var(--green)">Month</tspan></text>
    <text class="t-heavy" x="158" y="306" font-size="34" text-anchor="middle" fill="var(--green)">10-<tspan fill="var(--navy)">Gigs</tspan></text>

    <line x1="36" y1="371" x2="66" y2="371" stroke="var(--white)" stroke-width="1"/>
    <line x1="232" y1="371" x2="264" y2="371" stroke="var(--white)" stroke-width="1"/>
    <text class="t-semi" x="149" y="376" font-size="13" fill="var(--white)" text-anchor="middle">CHECK AVAILABILITY</text>

    <rect x="31" y="387" width="233" height="34" rx="17" fill="var(--green)"/>
    <circle cx="49" cy="404" r="12" fill="var(--white)"/>
    <path class="phone-icon" d="M44,398 c1,-1 2,-1 3,0 l1.5,2 c.5,1 0,1.5 -1,2 c.5,2 2,3.5 4,4 c.5,-1 1,-1.5 2,-1 l2,1.5 c1,1 1,2 0,3 c-3,2 -12,-3 -11.5,-11.5 z" fill="var(--navy)"/>
    <text class="t-bold" x="70" y="412" font-size="21" fill="var(--white)">(555) 014-2290</text>

    <circle cx="38" cy="437" r="7" fill="var(--white)"/>
    <circle cx="38" cy="437" r="4" fill="none" stroke="var(--navy)" stroke-width="1"/>
    <text class="t-regular" x="52" y="443" font-size="17" letter-spacing="2.5" fill="var(--white)">www.<tspan class="t-bold" fill="var(--green)">lumenpath</tspan>.net</text>

    <!-- address side -->
    <circle class="brand-dot" cx="393" cy="64" r="9" fill="var(--green)"/>
    <text class="brand-name t-bold" x="408" y="73" font-size="23" fill="var(--navy)">Lumen Path</text>

    <rect class="stamp-box" x="588" y="31" width="87" height="87" fill="none" stroke="var(--ink-line)" stroke-width="1"/>
    <g class="address-lines" stroke="var(--ink-line)" stroke-width="1">
      <line x1="416" y1="243" x2="675" y2="243"/>
      <line x1="416" y1="298" x2="675" y2="298"/>
      <line x1="416" y1="351" x2="675" y2="351"/>
    </g>
  </svg>
</section>

</body>
</html>
```